SnackHarbor!!! A Vending Machine Business Looking for an attractive website.

We are a vending machine business in Northern Michigan. We have changed our name and have rebranded our company. We would like an attractive website that shares who we are, what services we provide, the products we offer in our machines, along with a form businesses can fill out to see if they are a good fit for our company. I would like to have a Home Page, About SnackHarbor, Why Choose SnackHarbor?, Products & Services, Contact Us (With a Login Option), and a page with a questionnaire for thos interested in getting a FREE Vending Machine.

Target Market(s)

Businesses, Campgrounds, Schools, and many more in Northern Michigan

Industry/Entity Type

Vending Machines

Number of Pages Required

5+ page

Requirements
Must have
• An inviting and enticing Home Page. I want to get my potential clients engaged in our website.
Nice to have
• Possibly background photos from Northern Michigan
Should not have
• A corporate feel. I do not want a boring website.

```html
<!DOCTYPE html>
<html lang="en">
<head>
<meta charset="utf-8">
<title>SnackHarbor – Crave. Vend. Repeat.</title>
<link rel="stylesheet" href="https://fonts.googleapis.com/css2?family=Mouse+Memoirs&family=Outfit:wght@300;400;500;600;700;800&display=swap">
<style>
:root{
  --navy:#1f1d5c;
  --navy-deep:#18174d;
  --green:#2e5a26;
  --green-bright:#5cc14a;
  --grey:#f3f3f3;
  --text:#555;
  --white:#fff;
  --water:#1d4f8a;
}
*{box-sizing:border-box;margin:0;padding:0}
html,body{width:1200px;height:4827px;overflow:hidden}
body{position:relative;font-family:"Outfit",sans-serif;color:var(--text);background:var(--white)}
.abs{position:absolute}
.display{font-family:"Mouse Memoirs",sans-serif;font-weight:400;color:var(--navy);line-height:1}
.btn{position:absolute;display:flex;align-items:center;justify-content:center;border-radius:30px;font-weight:600;font-size:18px;text-transform:uppercase;text-decoration:none}
.btn-green{background:var(--green);color:var(--white)}
.btn-white{background:var(--white);color:var(--navy)}

/* hero */
.hero{position:absolute;left:0;top:0;width:1200px;height:662px;clip-path:polygon(0 0,100% 0,100% 572px,0 662px);
  background:radial-gradient(ellipse 520px 200px at 600px 440px,#2a6fae 0%,var(--water) 55%,transparent 80%),
  linear-gradient(180deg,#3a4f7a 0%,#2c4a6e 30%,#2f5f8f 55%,#4a5a3a 85%,#3d4a2e 100%)}
.brand{font-weight:800;font-size:40px;color:var(--white);letter-spacing:-.5px;display:flex;align-items:center;gap:12px}
.brand i{width:22px;height:22px;border-radius:50%;background:currentColor;display:block}
.topbar{position:absolute;right:112px;top:20px;display:flex;align-items:center;gap:30px;color:var(--white);font-size:17px;font-weight:500}
.login{border:2px solid var(--white);border-radius:24px;padding:9px 18px}
.nav{position:absolute;right:112px;top:78px;display:flex;gap:20px;color:var(--white);font-size:17px;font-weight:500}
.nav .active{color:var(--green-bright)}
.hero h1{position:absolute;left:0;width:1200px;top:196px;text-align:center;color:var(--white);font-size:84px}
.hero p{position:absolute;left:0;width:1200px;top:295px;text-align:center;color:var(--white);font-size:27px}

/* who */
.who-art{left:112px;top:675px;width:350px;height:520px}
h2.display{font-size:60px}
.body-copy{font-size:15.5px;line-height:27px;color:var(--text)}

/* why */
.grey{position:absolute;left:0;top:1120px;width:1200px;height:1490px;background:var(--grey);
  clip-path:polygon(0 223px,100% 0,100% 100%,0 1285px)}
.card{position:absolute;background:var(--white)}
.card.left-slant{clip-path:polygon(40px 0,100% 16px,100% 100%,30px 100%,0 40px)}
.card.right-slant{clip-path:polygon(0 20px,93% 0,100% 40px,97% 100%,0 100%)}
.card h3{font-size:22px;font-weight:500;color:#222;margin-bottom:14px}
.card p{font-size:15px;line-height:22px;color:var(--text)}
.card p b{color:var(--navy);font-weight:600}
.num{position:absolute;font-size:130px;font-weight:700;line-height:1}
.num.navy{color:var(--navy)}.num.green{color:var(--green)}

/* services */
.svc-list{left:110px;top:2755px;width:490px;list-style:none}
.svc-list li{display:flex;gap:14px;font-size:15.5px;line-height:24px;margin-bottom:24px}
.svc-list svg{flex:none;margin-top:3px}

/* products */
.products{position:absolute;left:0;top:3203px;width:1200px;height:722px;background:var(--navy);
  clip-path:polygon(0 0,100% 60px,100% 100%,0 100%)}
.prod{position:absolute;top:3566px;width:231px;height:270px;background:var(--white)}
.prod .ph{position:absolute;left:14px;top:14px;width:203px;height:193px}
.prod span{position:absolute;left:0;width:100%;top:228px;text-align:center;font-size:19px;font-weight:500;color:#222}

/* cta */
.cta{position:absolute;left:0;top:3924px;width:1200px;height:540px;background:var(--green);
  clip-path:polygon(0 0,100% 0,100% 416px,0 100%)}

/* footer */
.foot h4{font-size:19px;font-weight:600;color:#222;margin-bottom:22px}
.foot li{list-style:none;font-size:16px;line-height:30px;color:var(--text)}
.contact li{display:flex;align-items:center;gap:16px;line-height:30px;margin-bottom:30px}
.rule{left:112px;top:4725px;width:976px;height:1px;background:#ddd}
.social{top:4752px;width:40px;height:40px;border:2px solid var(--navy);border-radius:50%}
</style>
</head>
<body>

<header class="hero">
  <div role="img" aria-label="Aerial photo of a Northern Michigan bay and shoreline town" class="abs" style="inset:0"></div>
  <div class="brand abs" style="left:112px;top:34px"><i></i>SnackHarbor</div>
  <div class="topbar">
    <span>
      <svg width="16" height="16" viewBox="0 0 24 24" style="vertical-align:-2px;margin-right:6px"><path fill="#fff" d="M6.6 10.8a15 15 0 006.6 6.6l2.2-2.2c.3-.3.7-.4 1-.2 1.1.4 2.3.6 3.6.6.6 0 1 .4 1 1V20c0 .6-.4 1-1 1A17 17 0 013 4c0-.6.4-1 1-1h3.5c.6 0 1 .4 1 1 0 1.3.2 2.5.6 3.6.1.3 0 .7-.2 1z"/></svg>Call: 1 555 010 0142</span>
    <span class="login">&#9679; LOGIN</span>
  </div>
  <nav class="nav"><span class="active">Home</span><span>About</span><span>Why Choose SnackHarbor?</span><span>Services</span><span>Products</span><span>Contact Us</span></nav>
  <h1 class="display">SnackHarbor: Crave. Vend. Repeat.</h1>
  <p>Elevating Snacking, One Vend at a Time</p>
  <a class="btn btn-white" style="left:403px;top:370px;width:308px;height:63px;font-size:19px">Free Vending Machine</a>
</header>

<section class="who">
  <div class="abs who-art" role="img" aria-label="Illustration of a stylised navy vending machine stocked with snacks" style="background:linear-gradient(135deg,var(--navy) 0%,var(--navy) 40%,#3b3a7a 60%,#6a7e4a 100%);clip-path:polygon(8% 18%,55% 0,100% 8%,100% 82%,45% 95%,30% 100%,22% 70%,0 20%)"></div>
  <h2 class="display abs" style="left:548px;top:724px">Who We Are</h2>
  <p class="body-copy abs" style="left:548px;top:866px;width:545px">Welcome to SnackHarbor, where snacking meets delight! We're not just about vending machines; we're your culinary companions, your flavor curators, and your secret stash of happiness. Owen and Clara, the dynamic duo behind SnackHarbor, have a passion for all things tasty. With backgrounds in sales and a penchant for personal connections, they've transformed the vending experience into an art form.</p>
  <a class="btn btn-green" style="left:548px;top:1061px;width:138px;height:53px;font-size:17px">About Us</a>
</section>

<div class="grey"></div>
<section class="why">
  <h2 class="display abs" style="left:0;width:1200px;text-align:center;top:1334px">Why Choose SnackHarbor?</h2>

  <div class="num navy" style="left:198px;top:1518px">1</div>
  <div class="card left-slant" style="left:300px;top:1481px;width:788px;height:191px">
    <svg class="abs" style="left:50px;top:40px" width="100" height="90" viewBox="0 0 100 90" fill="none" stroke="var(--navy)" stroke-width="3"><path d="M50 28c-8-10-20-2-12 8l12 10 12-10c8-10-4-18-12-8z" stroke="var(--green)"/><circle cx="30" cy="52" r="6"/><circle cx="50" cy="56" r="6"/><circle cx="70" cy="52" r="6"/><path d="M20 80v-14l10-6 10 6v14M40 84v-14l10-6 10 6v14M60 80v-14l10-6 10 6v14"/></svg>
    <div class="abs" style="left:170px;top:38px;width:590px">
      <h3>Local Love</h3>
      <p>We celebrate the heart of Michigan by partnering with local legends. Say hello to Little <b>Ridgeline Jerky</b> and <b>Lakeshore Kettle Chips</b>—our hometown heroes. Their flavors dance on your taste buds, and we're thrilled to bring them straight to your workplace.</p>
    </div>
  </div>

  <div class="card right-slant" style="left:112px;top:1710px;width:788px;height:218px">
    <div class="abs" style="left:40px;top:46px;width:570px;text-align:right">
      <h3>Unleash Your Cravings</h3>
      <p>SnackHarbor isn't bound by corporate ties. We're the rebels of the vending world. Craving a bag of crispy, kettle-cooked chips? Done. Hankering for jerky that packs a punch? We've got you covered. Our machines are like treasure chests, waiting for you to unlock flavor magic.</p>
    </div>
    <svg class="abs" style="left:630px;top:40px" width="100" height="100" viewBox="0 0 100 100" fill="none" stroke="var(--navy)" stroke-width="3"><circle cx="50" cy="44" r="14"/><path d="M26 92c2-18 12-26 24-26s22 8 24 26"/><path d="M50 4v14M44 12l6 6 6-6M10 44h14M18 38l6 6-6 6M90 44H76M82 38l-6 6 6 6" stroke="var(--green)"/></svg>
  </div>
  <div class="num green" style="left:958px;top:1756px">2</div>

  <div class="num navy" style="left:200px;top:1980px">3</div>
  <div class="card left-slant" style="left:300px;top:1944px;width:788px;height:194px">
    <svg class="abs" style="left:56px;top:30px" width="90" height="90" viewBox="0 0 90 90" fill="none" stroke="var(--navy)" stroke-width="3.5"><path d="M45 4l10 8 13-1 3 12 11 7-5 12 5 12-11 7-3 12-13-1-10 8-10-8-13 1-3-12-11-7 5-12-5-12 11-7 3-12 13 1z"/><circle cx="45" cy="45" r="24"/><path d="M34 45l8 8 15-16" stroke="var(--green)"/></svg>
    <div class="abs" style="left:170px;top:32px;width:595px">
      <h3>Quality Meets Convenience</h3>
      <p>Imagine this: You're mid-meeting, and your stomach growls. Fear not! SnackHarbor's machines offer top-notch snacks and beverages. It's like having a mini food festival at your fingertips.<br><b>Tap to Pay:</b> No fumbling for change! SnackHarbor accepts tap-to-pay options, credit cards, and even phone wallets. Seamless snacking, guaranteed.</p>
    </div>
  </div>

  <div class="card right-slant" style="left:112px;top:2175px;width:788px;height:193px">
    <div class="abs" style="left:40px;top:58px;width:570px;text-align:right">
      <h3>Pandemic-Proof &amp; Recession-Ready</h3>
      <p>Life throws curveballs, but SnackHarbor stands strong. Our vending machines are the unsung heroes of resilience. Rain or shine, they're there, serving up joy.</p>
    </div>
    <svg class="abs" style="left:630px;top:42px" width="96" height="96" viewBox="0 0 96 96" fill="none" stroke="var(--navy)" stroke-width="3.5"><circle cx="48" cy="48" r="44"/><circle cx="48" cy="48" r="14" stroke="var(--green)"/><path d="M48 22v10M48 64v10M22 48h10M64 48h10M30 30l7 7M59 59l7 7M66 30l-7 7M30 66l7-7" stroke="var(--green)"/><path d="M18 18l60 60"/></svg>
  </div>
  <div class="num green" style="left:958px;top:2222px">4</div>
</section>

<section class="services">
  <h2 class="display abs" style="left:112px;top:2604px">Services We Provide</h2>
  <ul class="abs svc-list">
    <li><svg width="18" height="18" viewBox="0 0 18 18"><circle cx="9" cy="9" r="9" fill="var(--green)"/><path d="M5 9.5l3 3 5-6" stroke="#fff" stroke-width="2" fill="none"/></svg>We follow consumer trends as well as employ your feedback, ensuring that your machines are always filled with tasty options.</li>
    <li><svg width="18" height="18" viewBox="0 0 18 18"><circle cx="9" cy="9" r="9" fill="var(--green)"/><path d="M5 9.5l3 3 5-6" stroke="#fff" stroke-width="2" fill="none"/></svg>When we service your machines, we ensure quick and efficient service.</li>
    <li><svg width="18" height="18" viewBox="0 0 18 18"><circle cx="9" cy="9" r="9" fill="var(--green)"/><path d="M5 9.5l3 3 5-6" stroke="#fff" stroke-width="2" fill="none"/></svg>We perform routine maintenance including cleaning inside and outside of the machine.</li>
    <li><svg width="18" height="18" viewBox="0 0 18 18"><circle cx="9" cy="9" r="9" fill="var(--green)"/><path d="M5 9.5l3 3 5-6" stroke="#fff" stroke-width="2" fill="none"/></svg>We are committed to refreshing the assortment of products, keeping up with your customers needs.</li>
  </ul>
  <a class="btn btn-green" style="left:110px;top:3064px;width:160px;height:54px;font-size:17px">Read More</a>
  <div class="abs" role="img" aria-label="Photo of a snack vending machine beside a drinks vending machine" style="left:628px;top:2738px;width:572px;height:468px;background:linear-gradient(180deg,#2a2a2a 0%,#3c3c3c 62%,#c9c9c9 64%,#a9a9a9 95%,#1a1a1a 100%)"></div>
</section>

<section class="products">
  <div class="abs" role="img" aria-label="Faded photo of snacks inside a vending machine" style="inset:0;background:linear-gradient(180deg,rgba(255,255,255,.05),rgba(0,0,0,.1))"></div>
  <h2 class="display abs" style="left:0;width:1200px;text-align:center;top:204px;color:var(--white)">Products We Offer</h2>
</section>
<div class="prod" style="left:112px"><div class="ph" role="img" aria-label="Photo of canned and bottled drinks" style="background:linear-gradient(135deg,#dfe8f2,#b9c9e0)"></div><span>Thirsty?</span></div>
<div class="prod" style="left:360px"><div class="ph" role="img" aria-label="Photo of bags of chips" style="background:linear-gradient(135deg,#3b3b3b,#c9463a)"></div><span>Need the Crunch?</span></div>
<div class="prod" style="left:609px"><div class="ph" role="img" aria-label="Photo of candy bars" style="background:linear-gradient(135deg,#e9e4de,#4a5fa0)"></div><span>Guilty Pleasures</span></div>
<div class="prod" style="left:857px"><div class="ph" role="img" aria-label="Photo of assorted packaged snacks" style="background:linear-gradient(135deg,#d8e3c8,#c24a3a)"></div><span>Want Something More?</span></div>

<section class="cta">
  <h2 class="display abs" style="left:0;width:1200px;text-align:center;top:86px;color:var(--white);font-size:62px">Ready to experience the SnackHarbor difference?</h2>
  <p class="abs" style="left:0;width:1200px;text-align:center;top:212px;color:var(--white);font-size:15.5px;line-height:28px">Sign up now and let's connect. Taste the future of snacking firsthand! Contact us today<br>and explore how our vending magic can elevate your space.</p>
  <a class="btn btn-white" style="left:476px;top:302px;width:248px;height:66px;font-size:19px">Contact Us Today</a>
</section>

<footer class="foot">
  <div class="brand abs" style="left:103px;top:4560px;color:var(--navy);font-size:52px"><i></i>SnackHarbor</div>
  <div class="abs" style="left:532px;top:4464px">
    <h4>Quick Links</h4>
    <ul><li>Home</li><li>About</li><li>Why Choose SnackHarbor?</li><li>Services</li><li>Products</li><li>Contact Us</li></ul>
  </div>
  <div class="abs contact" style="left:816px;top:4464px">
    <h4>Contact Information</h4>
    <ul>
      <li><svg width="16" height="16" viewBox="0 0 24 24"><path fill="var(--navy)" d="M6.6 10.8a15 15 0 006.6 6.6l2.2-2.2c.3-.3.7-.4 1-.2 1.1.4 2.3.6 3.6.6.6 0 1 .4 1 1V20c0 .6-.4 1-1 1A17 17 0 013 4c0-.6.4-1 1-1h3.5c.6 0 1 .4 1 1 0 1.3.2 2.5.6 3.6.1.3 0 .7-.2 1z"/></svg>1 555 010 0142</li>
      <li><svg width="18" height="14" viewBox="0 0 18 14"><rect width="18" height="14" rx="1" fill="var(--navy)"/><path d="M1 2l8 6 8-6" stroke="#fff" stroke-width="1.5" fill="none"/></svg>info@snackharbor.com</li>
      <li><svg width="14" height="18" viewBox="0 0 14 18"><path fill="var(--navy)" d="M7 0a7 7 0 00-7 7c0 5 7 11 7 11s7-6 7-11a7 7 0 00-7-7zm0 10a3 3 0 110-6 3 3 0 010 6z"/></svg>Northern Michigan</li>
    </ul>
  </div>
  <div class="abs rule"></div>
  <p class="abs" style="left:112px;top:4762px;font-size:16px">© 2024 SnackHarbor. All rights reserved.</p>
  <span class="abs social" style="left:946px"></span>
  <span class="abs social" style="left:996px"></span>
  <span class="abs social" style="left:1046px"></span>
</footer>

</body>
</html>
```